Business Card Design needed for logo design project

Our business needs a business card design. I'm not sure what format files are generally delivered back, but clearly I will need the ability to edit to add colleagues contact details.

Our logo is attached.

Brivanor is a 3D design services company, providing app, serious/educational game, VR and AR websites/applications to corporate clients.

Target Market(s)

Corporate blue-chip clients needing 3D design services

Industry/Entity Type

Business

Font styles to use
Sans Serif

Requirements
Must have
• Templated such that I can add details (name, phone number etc). Needs to include logo from previous project winner - attached.

```html
<!DOCTYPE html>
<html lang="en">
<head>
<meta charset="utf-8">
<title>Brivanor Business Card</title>
<link rel="stylesheet" href="https://fonts.googleapis.com/css2?family=PT+Sans:ital,wght@0,400;0,700;1,400&display=swap">
<style>
  :root {
    --bg: #8d8e90;
    --brand-red: #d81a24;
    --brand-red-deep: #a3121b;
    --paper: #f4f4f2;
    --ink: #2b2b2b;
    --ink-soft: #4a4a4a;
    --white: #ffffff;
  }
  * { box-sizing: border-box; margin: 0; padding: 0; }
  html, body {
    width: 1200px; height: 955px; overflow: hidden;
    background: var(--bg);
    font-family: "PT Sans", sans-serif;
  }
  .canvas {
    position: relative; width: 1200px; height: 955px;
    display: flex; flex-direction: column; align-items: center; justify-content: center; gap: 60px;
  }
  .card {
    width: 630px; height: 360px; position: relative;
    box-shadow: 0 6px 18px rgba(0,0,0,0.25);
  }
  .card--front {
    background: radial-gradient(ellipse at 50% 40%, #e41d27 0%, var(--brand-red) 45%, var(--brand-red-deep) 100%);
    display: flex; align-items: center; justify-content: center;
  }
  .card--back { background: var(--paper); }

  .wordmark { display: flex; align-items: center; gap: 12px; }
  .wordmark__dot { width: 40px; height: 40px; border-radius: 50%; }
  .wordmark__name { font-size: 38px; font-weight: 400; letter-spacing: 2px; line-height: 1; }
  .card--front .wordmark__dot { background: var(--paper); }
  .card--front .wordmark__name { color: var(--paper); }
  .card--back .wordmark { position: absolute; left: 50px; top: 118px; }
  .card--back .wordmark__dot { background: var(--brand-red); }
  .card--back .wordmark__name { color: var(--ink); }

  .holder { position: absolute; right: 50px; top: 100px; text-align: left; width: 230px; }
  .holder__name { font-size: 26px; font-weight: 700; color: var(--ink); }
  .holder__role { font-size: 17px; font-style: italic; letter-spacing: 3px; color: var(--ink-soft); margin-top: 4px; }

  .contacts { position: absolute; left: 345px; top: 232px; list-style: none; }
  .contacts__item { display: flex; align-items: center; gap: 10px; font-size: 17px; color: var(--ink); height: 28px; }
  .contacts__icon { width: 20px; height: 20px; fill: var(--brand-red); flex: none; }
</style>
</head>
<body>
<main class="canvas">
  <section class="card card--front" aria-label="Card front">
    <div class="wordmark">
      <span class="wordmark__dot"></span>
      <span class="wordmark__name">BRIVANOR</span>
    </div>
  </section>

  <section class="card card--back" aria-label="Card back">
    <div class="wordmark">
      <span class="wordmark__dot"></span>
      <span class="wordmark__name">BRIVANOR</span>
    </div>

    <div class="holder">
      <p class="holder__name">Elias Marlowe</p>
      <p class="holder__role">Founder, CEO</p>
    </div>

    <ul class="contacts">
      <li class="contacts__item">
        <svg class="contacts__icon" viewBox="0 0 24 24" aria-hidden="true"><path d="M6.6 10.8a15.1 15.1 0 0 0 6.6 6.6l2.2-2.2a1 1 0 0 1 1-.25 11.4 11.4 0 0 0 3.6.57 1 1 0 0 1 1 1V20a1 1 0 0 1-1 1A17 17 0 0 1 3 4a1 1 0 0 1 1-1h3.5a1 1 0 0 1 1 1c0 1.25.2 2.45.57 3.57a1 1 0 0 1-.25 1z"/></svg>
        <span>0090 512 640 2718</span>
      </li>
      <li class="contacts__item">
        <svg class="contacts__icon" viewBox="0 0 24 24" aria-hidden="true"><path d="M2 5h20v14H2z M3.5 6.5 12 13l8.5-6.5" stroke="var(--paper)" stroke-width="1.4"/></svg>
        <span>info@brivanor.com</span>
      </li>
      <li class="contacts__item">
        <svg class="contacts__icon" viewBox="0 0 24 24" aria-hidden="true"><path d="M12 2a7 7 0 0 0-7 7c0 5.2 7 13 7 13s7-7.8 7-13a7 7 0 0 0-7-7zm0 9.5A2.5 2.5 0 1 1 12 6.5a2.5 2.5 0 0 1 0 5z"/></svg>
        <span>48C, Linden Row</span>
      </li>
    </ul>
  </section>
</main>
</body>
</html>
```